Safety training business card design

We need a buisness card design and logo for a small buisness that provides safety training through out the mining and civil construction industries. We provide first aid , confined space working at heights , machinery tickets, chainsaw, four wheel drive and four wheel motorbike training. We would like to use the design colors of navy blue, Fluro or lime green and white .

Industry/Entity Type

Construction

Contact Information for Business Card

Rillford Groundworks & Training , Neville Ormsby, rillford.skills@mailbox-example.net, ph 0481065374 abn 47 806 315 914

```html
<!DOCTYPE html>
<html lang="en">
<head>
<meta charset="utf-8">
<title>Rillford Groundworks &amp; Training – Business Card</title>
<link rel="stylesheet" href="https://fonts.googleapis.com/css2?family=Jura:wght@500;700&family=Michroma&display=swap">
<style>
  :root {
    --navy: #0b3777;
    --navy-deep: #082c62;
    --lime: #8cc21f;
    --white: #ffffff;
    --paper: #f3f4f6;
    --backdrop: #2b2b2d;
  }
  * { box-sizing: border-box; margin: 0; padding: 0; }
  html, body {
    width: 1200px;
    height: 848px;
    overflow: hidden;
    background: var(--backdrop);
  }
  .canvas {
    position: relative;
    width: 1200px;
    height: 848px;
    display: flex;
    align-items: center;
    justify-content: center;
    gap: 40px;
  }
  .card {
    position: relative;
    width: 540px;
    height: 309px;
    overflow: hidden;
    box-shadow: 0 14px 30px rgba(0,0,0,0.45);
  }

  /* Back side */
  .card--back {
    background: var(--navy);
    display: flex;
    align-items: center;
    justify-content: center;
  }
  .brand {
    display: flex;
    align-items: center;
    gap: 12px;
    font-family: "Jura", sans-serif;
    font-weight: 700;
  }
  .brand__dot {
    width: 16px;
    height: 16px;
    border-radius: 50%;
    background: var(--lime);
    flex: none;
  }
  .brand__name { line-height: 1.05; }
  .card--back .brand__name {
    color: var(--white);
    font-size: 30px;
  }

  /* Front side */
  .card--front { background: var(--white); }
  .band {
    position: absolute;
    left: 0;
    width: 100%;
    background: var(--navy);
  }
  .band--contact { top: 140px; height: 86px; }
  .band--lower { top: 238px; height: 52px; background: var(--navy-deep); }

  .card--front .brand {
    position: absolute;
    left: 34px;
    top: 40px;
    gap: 10px;
  }
  .card--front .brand__dot { width: 12px; height: 12px; }
  .card--front .brand__name {
    color: var(--navy);
    font-size: 17px;
  }

  .person-name {
    position: absolute;
    right: 28px;
    top: 110px;
    font-family: "Michroma", sans-serif;
    font-size: 17px;
    letter-spacing: 1px;
    color: var(--lime);
    text-transform: uppercase;
  }
  .contact-list {
    position: absolute;
    left: 232px;
    top: 150px;
    list-style: none;
    font-family: "Jura", sans-serif;
    font-weight: 500;
    font-size: 13px;
    color: var(--white);
  }
  .contact-list li {
    display: flex;
    align-items: center;
    gap: 10px;
    height: 22px;
    margin-bottom: 3px;
  }
  .contact-icon {
    width: 18px;
    height: 18px;
    flex: none;
  }
</style>
</head>
<body>
<main class="canvas">

  <section class="card card--back" aria-label="Card back">
    <div class="brand">
      <span class="brand__dot"></span>
      <span class="brand__name">Rillford<br>Groundworks &amp; Training</span>
    </div>
  </section>

  <section class="card card--front" aria-label="Card front">
    <div class="brand">
      <span class="brand__dot"></span>
      <span class="brand__name">Rillford<br>Groundworks<br>&amp; Training</span>
    </div>

    <div class="band band--contact"></div>
    <div class="band band--lower"></div>

    <h1 class="person-name">Neville Ormsby</h1>

    <ul class="contact-list">
      <li>
        <svg class="contact-icon" viewBox="0 0 18 18" aria-hidden="true">
          <rect width="18" height="18" rx="4" fill="#8cc21f"/>
          <circle cx="9" cy="9" r="2.4" fill="none" stroke="#0b3777" stroke-width="1.5"/>
          <path d="M11.4 7v3c0 1.3 2 1.3 2-0.6A4.6 4.6 0 1 0 11 13" fill="none" stroke="#0b3777" stroke-width="1.5" stroke-linecap="round"/>
        </svg>
        <span>rillford.skills@mailbox-example.net</span>
      </li>
      <li>
        <svg class="contact-icon" viewBox="0 0 18 18" aria-hidden="true">
          <rect width="18" height="18" rx="4" fill="#8cc21f"/>
          <path d="M6 4.2l1.8-0.6 1.2 2.6-1.2 1c0.6 1.4 1.6 2.4 3 3l1-1.2 2.6 1.2-0.6 1.8c-4.2 0.4-8.2-3.6-7.8-7.8z" fill="#0b3777"/>
        </svg>
        <span>0481065374</span>
      </li>
      <li>
        <svg class="contact-icon" viewBox="0 0 18 18" aria-hidden="true">
          <rect width="18" height="18" rx="4" fill="#8cc21f"/>
          <circle cx="9" cy="9" r="5" fill="none" stroke="#0b3777" stroke-width="1.3"/>
          <ellipse cx="9" cy="9" rx="2.2" ry="5" fill="none" stroke="#0b3777" stroke-width="1.1"/>
          <path d="M4 9h10M5 6.3h8M5 11.7h8" stroke="#0b3777" stroke-width="1"/>
        </svg>
        <span>ABN 47 806 315 914</span>
      </li>
    </ul>
  </section>

</main>
</body>
</html>
```